Lanterne architecture business cards

We are a new company based in New Zealand. We Specialize in High end Luxury Residential Architecture.

Every home is bespoke and is designed to each clients individual requirements and needs.

I like to design buildings that inspire people through light and form while offering a high level of comfort and usability.

Lines of sight, proportion and balance are fundamental to the spaces I create.
Updates

August 5th is current deadline - Today's date is the 13th of August.

Target Market(s)

New Zealanders who want a custom individual home design, typically 30-65 year old males and females

Industry/Entity Type

Architecture

Contact Information for Business Card

Director - Derek Tolson
Contact Number - 0279164073
Email - info@lanternearchitecture-example.co.nz
Webstie - www.lanternearchitecture-example.co.nz
Social Media - @lanternearchitecture

Font styles to use
Sans Serif

Requirements
Must have
• Logo (Both Sides)
Website
Email
Contact Number
Social Media

Nice to have
• Texture
Should not have
• More than 3 colours - typically I would've thought 2 would be good to match the logo.

```html
<!DOCTYPE html>
<html lang="en">
<head>
<meta charset="utf-8">
<title>Lanterne architecture – business cards</title>
<link rel="stylesheet" href="https://fonts.googleapis.com/css2?family=Montserrat:wght@300;400;600&display=swap">
<style>
  :root {
    --backdrop: #2b2828;
    --card-dark: #1c1c1c;
    --card-light: #f7f7f5;
    --ink-dark: #1a1a1a;
    --ink-light: #e6e6e6;
    --rule: #3a3a3a;
  }
  * { box-sizing: border-box; margin: 0; padding: 0; }
  html, body {
    width: 1200px; height: 901px; overflow: hidden;
    background: var(--backdrop);
    font-family: "Montserrat", sans-serif;
  }
  .canvas {
    width: 1200px; height: 901px;
    display: flex; flex-direction: column;
    align-items: center; justify-content: center; gap: 46px;
  }
  .card {
    width: 620px; height: 354px; position: relative;
    box-shadow: 0 10px 28px rgba(0,0,0,.45);
  }
  .card--front {
    background: var(--card-dark);
    display: flex; align-items: center; justify-content: center;
  }
  .wordmark {
    font-weight: 300; text-transform: uppercase; text-align: center;
    line-height: 1.6;
  }
  .card--front .wordmark {
    color: var(--ink-light); font-size: 30px; letter-spacing: 18px;
  }
  .card--back { background: var(--card-light); color: var(--ink-dark); }
  .card--back .wordmark {
    position: absolute; left: 52px; top: 52px;
    font-size: 15px; letter-spacing: 9px; text-align: left;
    color: var(--ink-dark);
  }
  .holder {
    position: absolute; right: 48px; top: 70px; text-align: right;
  }
  .holder__name {
    font-weight: 600; font-size: 24px; letter-spacing: .5px;
    text-transform: uppercase;
  }
  .holder__role { font-weight: 400; font-size: 15px; margin-top: 2px; }
  .divider {
    position: absolute; left: 52px; right: 48px; top: 170px;
    height: 1px; background: var(--rule);
  }
  .contacts {
    position: absolute; left: 52px; top: 196px; list-style: none;
    font-size: 16px; font-weight: 400; line-height: 1.55;
  }
  .contacts li { display: flex; align-items: center; gap: 10px; }
  .contacts svg { width: 13px; height: 13px; flex: none; }
</style>
</head>
<body>
<main class="canvas">
  <section class="card card--front" aria-label="Card front">
    <p class="wordmark">Lanterne<br>architecture</p>
  </section>

  <section class="card card--back" aria-label="Card back">
    <p class="wordmark">Lanterne<br>architecture</p>
    <div class="holder">
      <p class="holder__name">Derek Tolson</p>
      <p class="holder__role">Director</p>
    </div>
    <div class="divider"></div>
    <ul class="contacts">
      <li>
        <svg viewBox="0 0 16 16" aria-hidden="true"><path d="M3 1.5l3 3-1.6 1.6a9 9 0 0 0 5.5 5.5L11.5 10l3 3-1.8 2C6.5 15 1 9.5 1 3.3z" fill="#1a1a1a"/></svg>
        0279164073
      </li>
      <li>
        <svg viewBox="0 0 16 16" aria-hidden="true"><rect x="1" y="3" width="14" height="10" fill="none" stroke="#1a1a1a" stroke-width="1.5"/><path d="M1 3l7 6 7-6" fill="none" stroke="#1a1a1a" stroke-width="1.5"/></svg>
        info@lanternearchitecture-example.co.nz
      </li>
      <li>
        <svg viewBox="0 0 16 16" aria-hidden="true"><circle cx="8" cy="8" r="6.5" fill="none" stroke="#1a1a1a" stroke-width="1.4"/><ellipse cx="8" cy="8" rx="3" ry="6.5" fill="none" stroke="#1a1a1a" stroke-width="1.2"/><path d="M1.5 8h13" stroke="#1a1a1a" stroke-width="1.2"/></svg>
        www.lanternearchitecture-example.co.nz
      </li>
      <li>
        <svg viewBox="0 0 16 16" aria-hidden="true"><rect x="2" y="2" width="12" height="12" fill="#1a1a1a"/></svg>
        @lanternearchitecture
      </li>
    </ul>
  </section>
</main>
</body>
</html>
```